Business card design for Velvet Harbor

We need business cards designed for our new marketing consulting company, Velvet Harbor. Our services include marketing strategy, go-to-market and launch planning, growth strategy, and execution. We serve medical technology and health technology companies, from startups to well-established growth companies.

The business cards should feel professional, credible, reliable and trustworthy, and should instill confidence. Also bold, creative, and modern.

The design must use the Velvet Harbor logo.

The primary brand color is this orange: #FF5501
A secondary color that you can use is this gray: #282B2D
I would prefer only to use the orange and gray. But if you feel you really need an additional accent color (please use it very sparingly, as little as possible), you can use this blue for small accent purposes: #009FED

Attached are the logo files. The main logo is the one with a little bit of orange on the left and the rest is gray.

The business card should include the following:

Velvet Harbor logo
First name and last name
Title
Email address
Phone number and type (in whatever order looks best for the design
Website (the website does not need to be in the same block as the personal info)

For example:

Nessa Pryle
Founder & Principal
nessa@velvetharbor.com
+1.628.309.4156 mobile (can use "." or spaces in between blocks of numbers)
velvetharbor.com (somewhere on the card, it does not need to be with the personal info; and note that there is no "www." at the beginning)

Note that there will be no address listed on the business card.

Target Market(s)

Executives (CEO, head of marketing, head of sales) at medical technology and health technology companies, mostly in their 40s and older, well-educated, often with advanced degrees. They are strategic thinkers, responsible for budgets, and familiar with P&L. Their comfort with and trust in using outside consultants varies.

Industry/Entity Type

Medical technology and health technology companies.

Contact Information for Business Card

See project description

Font styles to use
Sans Serif

Requirements
Must have
• Logo and see Business card details section above.

```html
<!DOCTYPE html>
<html lang="en">
<head>
<meta charset="utf-8">
<title>Velvet Harbor – Business Card</title>
<link href="https://fonts.googleapis.com/css2?family=Michroma&family=Montserrat:wght@400;500;600&display=swap" rel="stylesheet">
<style>
  :root {
    --orange: #FF5501;
    --card: #282B2D;
    --backdrop: #161718;
    --text: #F2F2F2;
    --muted: #8A8F94;
  }
  * { box-sizing: border-box; margin: 0; padding: 0; }
  html, body {
    width: 1200px; height: 897px; overflow: hidden;
    background: var(--backdrop);
    font-family: "Montserrat", sans-serif;
    color: var(--text);
  }
  .canvas { position: relative; width: 1200px; height: 897px; }
  .card {
    position: absolute; left: 303px; width: 594px; height: 339px;
    background: var(--card); border-radius: 16px;
  }
  .card--front { top: 92px; }
  .card--back { top: 469px; }

  .brand {
    position: absolute; left: 32px; top: 42px;
    display: flex; align-items: center; gap: 12px;
  }
  .brand__dot { width: 14px; height: 14px; border-radius: 50%; background: var(--orange); }
  .brand__name {
    font-weight: 600; font-size: 20px; line-height: 24px;
    letter-spacing: 4px; text-transform: uppercase; color: var(--text);
    width: 150px;
  }

  .person { position: absolute; left: 32px; top: 188px; }
  .person__name {
    font-family: "Michroma", sans-serif; font-size: 19px;
    letter-spacing: 3px; color: var(--orange); text-transform: uppercase;
  }
  .person__title { font-size: 15px; margin-top: 2px; }

  .divider {
    position: absolute; left: 32px; top: 240px; width: 530px;
    height: 1px; background: var(--orange);
  }

  .contact {
    position: absolute; left: 32px; top: 256px;
    list-style: none; font-size: 14.5px; line-height: 18px;
  }
  .contact li { display: flex; align-items: center; gap: 4px; }
  .contact svg { width: 10px; height: 10px; flex: none; }

  .services {
    position: absolute; right: 32px; top: 258px;
    list-style: none; font-size: 14px; line-height: 18px; text-align: right;
  }
  .services li { display: flex; justify-content: flex-end; align-items: center; gap: 6px; }
  .services li::after {
    content: ""; width: 7px; height: 7px; border-radius: 50%;
    border: 1.5px solid var(--orange);
  }

  .brand--back {
    left: 50%; top: 50%; transform: translate(-50%, -50%); gap: 22px;
  }
  .brand--back .brand__dot { width: 30px; height: 30px; }
  .brand--back .brand__name {
    width: auto; font-size: 40px; line-height: 46px; letter-spacing: 10px;
    color: var(--muted);
  }
</style>
</head>
<body>
<main class="canvas">
  <section class="card card--front">
    <div class="brand">
      <span class="brand__dot"></span>
      <span class="brand__name">Velvet Harbor</span>
    </div>

    <div class="person">
      <h1 class="person__name">Nessa Pryle</h1>
      <p class="person__title">Founder &amp; Principal</p>
    </div>

    <div class="divider"></div>

    <ul class="contact">
      <li>
        <svg viewBox="0 0 10 10" aria-hidden="true"><path d="M2 1l2 2-1 1.2c.6 1.2 1.6 2.2 2.8 2.8L7 6l2 2-1.2 1.4C4.5 9 1 5.5.6 2.2z" fill="none" stroke="var(--orange)" stroke-width="1"/></svg>
        +1.628.309.4156
      </li>
      <li>
        <svg viewBox="0 0 10 10" aria-hidden="true"><rect x="0.6" y="2" width="8.8" height="6" fill="none" stroke="var(--orange)" stroke-width="1"/><path d="M.6 2L5 5.5 9.4 2" fill="none" stroke="var(--orange)" stroke-width="1"/></svg>
        nessa@velvetharbor.com
      </li>
      <li>
        <svg viewBox="0 0 10 10" aria-hidden="true"><circle cx="5" cy="5" r="4.4" fill="none" stroke="var(--orange)" stroke-width="1"/><ellipse cx="5" cy="5" rx="2" ry="4.4" fill="none" stroke="var(--orange)" stroke-width="0.8"/><path d="M.6 5h8.8" stroke="var(--orange)" stroke-width="0.8"/></svg>
        www.velvetharbor.com
      </li>
    </ul>

    <ul class="services">
      <li>marketing strategy</li>
      <li>go-to-market and launch planning</li>
      <li>growth strategy, and execution</li>
    </ul>
  </section>

  <section class="card card--back">
    <div class="brand brand--back">
      <span class="brand__dot"></span>
      <span class="brand__name">Velvet Harbor</span>
    </div>
  </section>
</main>
</body>
</html>
```